Talbrin Business Cards

Front and back. Simon Kavelle MBA is the CEO of Talbrin Homes. Black white and grays. Logo and cool design.

Target Market(s)

Professional lenders and investors

Industry/Entity Type

Real estate developer. NO HOUSES OR ROOFS

Contact Information for Business Card

Logo, name and unique design. Front and back. Simon Kavelle MBA is the CEO of Talbrin Homes. Black white and grays. Logo and cool design.

Font styles to use
Sans Serif

Colors

Designer to choose only greyscale colors for use in the design.

Requirements
Must have
• Cool look. Not the same card I could design.
Nice to have
• Something memorable
Should not have
• Basic

```html
<!DOCTYPE html>
<html lang="en">
<head>
<meta charset="utf-8">
<title>Talbrin Homes — Business Card</title>
<link rel="stylesheet" href="https://fonts.googleapis.com/css2?family=Poppins:wght@300;400;800&display=swap">
<style>
  :root {
    --stage: #161616;
    --card: #070707;
    --ink-light: #ffffff;
    --ink-soft: #d9d9d9;
    --tone-black: #080808;
    --tone-graphite: #2a2a2a;
    --tone-silver: #b9b9b9;
    --tone-pale: #e4e4e4;
    --logo-ink: #070707;
  }
  * { box-sizing: border-box; margin: 0; padding: 0; }
  html, body {
    width: 1200px;
    height: 900px;
    overflow: hidden;
    background: var(--stage);
    font-family: "Poppins", sans-serif;
  }
  .stage {
    width: 1200px;
    height: 900px;
    display: flex;
    flex-direction: column;
    align-items: center;
    justify-content: center;
    gap: 48px;
  }
  .card {
    position: relative;
    width: 600px;
    height: 343px;
    background: var(--card);
    overflow: hidden;
    box-shadow: 0 22px 48px rgba(0, 0, 0, 0.6);
  }
  .pattern-field {
    position: absolute;
    background: linear-gradient(118deg,
      var(--tone-black) 0%,
      var(--tone-silver) 14%,
      var(--tone-graphite) 27%,
      var(--tone-pale) 41%,
      var(--tone-black) 54%,
      var(--tone-silver) 68%,
      var(--tone-graphite) 82%,
      var(--tone-pale) 94%,
      var(--tone-black) 100%);
  }
  .card--front .pattern-field { inset: 0; }
  .logo-plate {
    position: absolute;
    left: 50%;
    top: 50%;
    transform: translate(-50%, -50%);
    width: 270px;
    height: 112px;
    background: var(--ink-light);
    display: flex;
    align-items: center;
    justify-content: center;
  }
  .logo-name {
    font-weight: 800;
    font-size: 31px;
    letter-spacing: -0.8px;
    color: var(--logo-ink);
  }
  .card--back .pattern-field {
    left: 0; right: 0; top: 0;
    height: 178px;
    background: linear-gradient(172deg,
      var(--tone-silver) 0%,
      var(--tone-graphite) 22%,
      var(--tone-pale) 45%,
      var(--tone-graphite) 68%,
      var(--tone-silver) 84%,
      var(--card) 100%);
  }
  .holder {
    position: absolute;
    left: 34px;
    bottom: 30px;
    color: var(--ink-light);
    line-height: 1.08;
  }
  .holder-name {
    font-weight: 800;
    font-size: 27px;
  }
  .holder-credential { font-weight: 300; }
  .holder-role {
    margin-top: 6px;
    font-weight: 300;
    font-size: 13px;
    color: var(--ink-soft);
    letter-spacing: 0.5px;
  }
  .contact {
    position: absolute;
    right: 34px;
    bottom: 34px;
    text-align: right;
    list-style: none;
    font-weight: 300;
    font-size: 13px;
    line-height: 1.55;
    color: var(--ink-soft);
  }
  .contact li:first-child { margin-bottom: 12px; }
</style>
</head>
<body>
  <main class="stage">
    <section class="card card--front" aria-label="Card front">
      <div class="pattern-field" role="img" aria-label="Dense pattern of looping silver and white flowing lines over black, covering the whole card"></div>
      <div class="logo-plate">
        <span class="logo-name">Talbrin Homes</span>
      </div>
    </section>

    <section class="card card--back" aria-label="Card back">
      <div class="pattern-field" role="img" aria-label="Band of looping silver and white flowing lines over black across the upper card"></div>
      <div class="holder">
        <p class="holder-name">Simon<br>Kavelle <span class="holder-credential">MBA</span></p>
        <p class="holder-role">CEO</p>
      </div>
      <ul class="contact">
        <li>(555) 010 482</li>
        <li>info@talbrinhomes.com</li>
        <li>www.talbrinhomes.com</li>
      </ul>
    </section>
  </main>
</body>
</html>
```